Business card design for holistic health care clinic

We need a double-sided business card design for our holistic health care clinic that integrates our logo design and also its color scheme. My business is called Veralune. It is an integrative medicine clinic. You have already done the logo for me. Please ensure an elegant and upscale design that is not cluttered, but still has all the necessary information (please see below for details).

Target Market(s)

Wellness, fitness, rehabilitation for educated, well-traveled open-minded clients who are focused on natural, organic, balanced and preventive healthcare and lifestyle.

Industry/Entity Type

Medical

Contact Information for Business Card

Modern, clean.

Number of Pages Required

1 page

Font styles to use
Serif
Sans Serif

Colors

Designer to choose colors to be used in the design.

Requirements
Must have
• Logo on one side, all other information on the other side.
• Other information should include:
• Tobias Wendmere - DOE, CPT, LMT
• 1450 North Calloway Street
• Austin, TX 78744
• 512 555 0184
• 818 555 0127
• info@VeraluneHealth.com
• t.wendmere@VeraluneHealth.com
Nice to have
• Darker background on front - but not totally black - shaded/dark gray.

```html
<!DOCTYPE html>
<html lang="en">
<head>
<meta charset="utf-8">
<title>Veralune Business Card</title>
<link rel="stylesheet" href="https://fonts.googleapis.com/css2?family=Nunito:wght@800&family=Nunito+Sans:wght@400;700&display=swap">
<style>
  :root {
    --backdrop: #5e5e5e;
    --card-light: #ffffff;
    --card-dark: #38383b;
    --brand-blue: #1b95d3;
    --ink: #1c1c1c;
    --body-ink: #2a2a2a;
  }
  * { box-sizing: border-box; margin: 0; padding: 0; }
  html, body {
    width: 1200px; height: 1200px; overflow: hidden;
    background: var(--backdrop);
  }
  .sheet {
    position: relative; width: 1200px; height: 1200px;
    display: flex; align-items: center; justify-content: center; gap: 16px;
  }
  .card {
    width: 533px; height: 298px; border-radius: 10px;
    position: relative; overflow: hidden;
  }
  .card--back { background: var(--card-light); }
  .card--front { background: var(--card-dark); }

  .wordmark {
    font-family: "Nunito", sans-serif; font-weight: 800;
    color: var(--brand-blue); letter-spacing: 0.5px; line-height: 1;
  }
  .tagline {
    font-family: "Nunito", sans-serif; font-weight: 800;
    color: var(--brand-blue); line-height: 1; white-space: nowrap;
  }

  .back-logo {
    position: absolute; left: 22px; top: 124px; width: 214px; text-align: center;
  }
  .back-logo .wordmark { font-size: 40px; }
  .back-logo .tagline { font-size: 12px; margin-top: 6px; }

  .contact {
    position: absolute; left: 254px; top: 46px; right: 18px;
    font-family: "Nunito Sans", sans-serif; color: var(--body-ink);
    white-space: nowrap;
  }
  .contact__name {
    font-family: "Nunito", sans-serif; font-weight: 800;
    font-size: 22px; color: var(--ink); line-height: 1.1;
  }
  .contact__credentials {
    font-size: 13.5px; color: var(--brand-blue); margin-top: 4px; letter-spacing: 0.3px;
  }
  .contact__rule {
    width: 24px; height: 2px; background: var(--ink); margin: 13px 0 26px;
  }
  .contact__list { list-style: none; }
  .contact__item {
    display: flex; align-items: center; gap: 7px;
    font-size: 15px; line-height: 20.8px;
  }
  .contact__item svg { width: 13px; height: 13px; flex: none; }
  .contact__address { font-size: 15px; line-height: 20.8px; margin-top: 11px; }

  .front-logo {
    position: absolute; inset: 0;
    display: flex; flex-direction: column; align-items: center; justify-content: center;
    padding-top: 14px;
  }
  .front-logo .wordmark { font-size: 60px; }
  .front-logo .tagline { font-size: 17px; margin-top: 8px; }
</style>
</head>
<body>
  <main class="sheet">
    <section class="card card--back" aria-label="Business card, contact side">
      <div class="back-logo">
        <div class="wordmark">Veralune</div>
        <div class="tagline">Integrative Holistic Medicine</div>
      </div>
      <div class="contact">
        <h1 class="contact__name">Tobias Wendmere</h1>
        <p class="contact__credentials">DOE, CPT, LMT</p>
        <div class="contact__rule"></div>
        <ul class="contact__list">
          <li class="contact__item">
            <svg viewBox="0 0 13 13" aria-hidden="true"><rect x="3" y="0.8" width="7" height="11.4" rx="1.2" fill="none" stroke="#1b95d3" stroke-width="1"/><line x1="5.5" y1="10.3" x2="7.5" y2="10.3" stroke="#1b95d3" stroke-width="0.9"/></svg>
            512 555 0184
          </li>
          <li class="contact__item">
            <svg viewBox="0 0 13 13" aria-hidden="true"><path d="M3 1.2 L5 3.6 L3.9 5.1 Q5.4 8 7.9 9.1 L9.4 8 L11.8 10 L10.4 11.8 Q6 11.6 3.2 8.3 Q1 5.4 1.3 2.6 Z" fill="none" stroke="#1b95d3" stroke-width="0.9" stroke-linejoin="round"/></svg>
            818 555 0127
          </li>
          <li class="contact__item">
            <svg viewBox="0 0 13 13" aria-hidden="true"><rect x="1" y="3" width="11" height="7.5" fill="none" stroke="#1b95d3" stroke-width="0.9"/><path d="M1 3 L6.5 7.5 L12 3 M1 10.5 L5 6.5 M12 10.5 L8 6.5" fill="none" stroke="#1b95d3" stroke-width="0.9"/></svg>
            info@VeraluneHealth.com
          </li>
          <li class="contact__item">
            <svg viewBox="0 0 13 13" aria-hidden="true"><rect x="1" y="3" width="11" height="7.5" fill="none" stroke="#1b95d3" stroke-width="0.9"/><path d="M1 3 L6.5 7.5 L12 3 M1 10.5 L5 6.5 M12 10.5 L8 6.5" fill="none" stroke="#1b95d3" stroke-width="0.9"/></svg>
            t.wendmere@VeraluneHealth.com
          </li>
        </ul>
        <p class="contact__address">1450 North Calloway Street<br>Austin, TX 78744</p>
      </div>
    </section>

    <section class="card card--front" aria-label="Business card, logo side">
      <div class="front-logo">
        <div class="wordmark">Veralune</div>
        <div class="tagline">Integrative Holistic Medicine</div>
      </div>
    </section>
  </main>
</body>
</html>
```